Hand-Crafted Furniture Company

We are working with Brammvok to build a new website for them.

Some sites to use for content/competitors and inspiration:

https://quintalfurniture.example
https://ashbelhome.example
https://www.pelgravik.example
https://www.dunsmarewoodworks.example

Thank you for taking the time to consider designing a website for us. We are web developers based in Stockton, CA, USA. Most of our projects go through the same process. Understanding this process may help you win a project with us. We custom-code all of our websites in-house. We don’t have any requirements as to what tools you use for your design, but we prefer Figma files. For any design that we label as four stars, we send it to the client for review. The client picks the final design they want us to use. Once we complete this process, we will continue to show additional clients all the four-star sites and purchase them later. Your designs will have multiple chances to sell. For better chances of success, we ask that you follow these guidelines.

IMAGES:
If you use any images or icons in the design, we ask that you have a link to the asset so we can purchase the image/icon. Most of the designs we submit do not have the customer’s images on them unless they have some great images. Be creative; show us the feeling you are trying to portray with your image choices. Use any royalty-free site you choose. We subscribe to Adobe and mainly use their images, but we can purchase images outside of Adobe. PLEASE NOTE: we will not submit designs to clients with watermarks on the images.

FONTS:
We ask that you identify the fonts used in the design. This can be done in a message if you want. We typically use Google Fonts and Adobe Fonts.

CONTENT:
We're always open to different content and ideas. We often submit designs with stock images so the client can see our vision. We typically take pictures after the website launch to use their images with our vision. Lorem Ipsum is fine for paragraphs, but we ask that you write the headers in correct English. We want to be able to show the vision and identify the sections of the website.

INSPIRATION:
We typically add a couple of links in the brief of websites we like to help you get started in your design.

REVISIONS:
We do not often ask for revisions of the designs unless we see something in the design that may not appeal to the client. If there are slight changes that we want to make, we do that in the development process.

FEEDBACK:
We rarely give feedback on designs during the design process. We are working on many website projects and do not have the time to provide feedback. We usually respond if your request is well thought out and asks specific questions, but a note asking “feedback, please” usually goes unanswered.

```html
<!DOCTYPE html>
<html lang="en">
<head>
<meta charset="UTF-8">
<title>Brammvok — Hand-Crafted Furniture</title>
<link href="https://fonts.googleapis.com/css2?family=Archivo:wght@400;500;600;700;800&family=Inter:wght@400;500;600&display=swap" rel="stylesheet">
<style>
  :root{
    --brown:#4e3524;
    --brown-deep:#3a2619;
    --tan:#c39c70;
    --cream:#f4f0ea;
    --card:#f3eee6;
    --ink:#1d1d1d;
    --muted:#6b6b6b;
    --white:#ffffff;
    --black:#050505;
  }
  *{margin:0;padding:0;box-sizing:border-box}
  html,body{width:1200px;height:3668px;overflow:hidden;background:var(--white)}
  body{position:relative;font-family:"Inter",sans-serif;color:var(--ink)}
  .abs{position:absolute}
  h1,h2,h3,h4,.btn,.nav a,.logo{font-family:"Archivo",sans-serif}

  /* header */
  .logo{position:absolute;left:112px;top:24px;font-size:40px;font-weight:700;color:var(--brown);letter-spacing:-.5px;line-height:1}
  .nav{position:absolute;left:414px;top:24px;display:flex;gap:6px}
  .nav a{font-size:15px;font-weight:500;color:var(--ink);text-decoration:none;padding:8px 12px;border-radius:6px}
  .nav a.active{background:var(--brown);color:var(--white)}
  .btn{display:inline-flex;align-items:center;justify-content:center;border-radius:30px;font-weight:600;font-size:14px;letter-spacing:.3px;text-decoration:none;color:var(--white);background:var(--brown)}
  .login{position:absolute;left:904px;top:18px;width:100px;height:40px}
  .cart{position:absolute;left:1024px;top:20px;display:flex;align-items:center;gap:6px;font-size:11px;font-weight:600}
  .cart-dot{width:34px;height:34px;border-radius:50%;background:var(--brown);display:flex;align-items:center;justify-content:center}

  /* hero */
  .hero{position:absolute;left:16px;top:88px;width:1168px;height:564px;border-radius:14px;overflow:hidden;
    background:linear-gradient(90deg,#2a1b14 0%,#6e3a24 35%,#a4532f 55%,#c98a5e 75%,#6d4b33 100%)}
  .hero-shade{position:absolute;inset:0;background:linear-gradient(90deg,rgba(0,0,0,.55) 0%,rgba(0,0,0,.15) 50%,rgba(0,0,0,0) 100%)}
  .hero-text{position:absolute;left:96px;top:132px;color:var(--white)}
  .hero-text .eyebrow{font-size:26px;font-weight:400;margin-bottom:8px}
  .hero-text h1{font-size:54px;font-weight:500;line-height:1.08}
  .hero-text p{font-size:17px;margin-top:12px}
  .hero-text .btn{margin-top:28px;width:148px;height:50px;font-size:14px}

  /* section headings */
  .section-title{position:absolute;left:0;width:1200px;text-align:center;font-size:34px;font-weight:700;letter-spacing:.5px}

  /* tabs */
  .tabs{position:absolute;top:792px;left:0;width:1200px;display:flex;justify-content:center;gap:26px}
  .tab{width:164px;height:48px;border-radius:30px;background:var(--cream);font-family:"Archivo",sans-serif;font-size:13px;font-weight:500;display:flex;align-items:center;justify-content:center}
  .tab.active{background:var(--brown);color:var(--white)}

  /* category cards */
  .cat{position:absolute;top:904px;width:290px;height:456px;background:var(--card);border-radius:10px;text-align:center}
  .cat h3{margin-top:44px;font-size:28px;font-weight:600;letter-spacing:.5px}
  .cat .count{font-size:12px;margin-top:10px;font-family:"Archivo",sans-serif}
  .cat .btn{margin-top:18px;width:118px;height:40px;font-size:13px}
  .cat .photo{position:absolute;left:20px;right:20px;bottom:18px;height:210px;border-radius:8px}

  /* feature tiles */
  .tile{position:absolute;top:1480px;width:440px;height:420px;border-radius:12px;overflow:hidden}
  .tile .label{position:absolute;left:40px;top:268px;color:var(--white);font-family:"Archivo",sans-serif;font-size:34px;font-weight:400}
  .tile .btn{position:absolute;left:40px;top:330px;width:118px;height:40px;font-size:12px}
  .tile .dim{position:absolute;inset:0;background:linear-gradient(0deg,rgba(0,0,0,.45),rgba(0,0,0,0) 60%)}

  /* about */
  .about{position:absolute;left:0;top:1988px;width:1200px;height:584px;background:var(--cream)}
  .about .photo{position:absolute;left:112px;top:92px;width:450px;height:400px;border-radius:10px;
    background:linear-gradient(135deg,#3a2a20 0%,#7a5236 45%,#2b1f18 100%)}
  .about h2{position:absolute;left:592px;top:112px;font-size:36px;font-weight:700;line-height:1.15;letter-spacing:.3px}
  .about .copy{position:absolute;left:592px;top:208px;width:500px;font-size:15px;line-height:1.5;color:#333}
  .about .copy p+p{margin-top:18px}
  .about .btn{position:absolute;left:592px;top:420px;width:184px;height:56px;background:var(--tan);font-size:14px}

  /* blog */
  .post{position:absolute;top:2740px;width:312px;text-align:center}
  .post .photo{height:240px;border-radius:10px}
  .post h4{margin-top:20px;font-size:18px;font-weight:500;line-height:1.3}
  .post .date{margin-top:16px;font-size:11px;color:var(--muted)}
  .post .more{margin-top:10px;font-family:"Archivo",sans-serif;font-size:13px;font-weight:600}

  /* footer */
  .footer{position:absolute;left:0;top:3224px;width:1200px;height:444px;background:var(--black);color:var(--white)}
  .footer .logo{left:112px;top:80px;color:var(--tan);font-size:40px}
  .footer .about-text{position:absolute;left:112px;top:160px;width:340px;font-size:14px;line-height:1.6;color:#e6e6e6}
  .fcol{position:absolute;top:64px}
  .fcol h4{font-size:20px;font-weight:700;letter-spacing:.5px;padding-bottom:8px;position:relative}
  .fcol h4::after{content:"";position:absolute;left:0;bottom:0;width:44px;height:2px;background:var(--white)}
  .fcol ul{list-style:none;margin-top:14px}
  .fcol li{font-size:14px;line-height:30px;color:#e6e6e6}
  .footer .rule{position:absolute;left:112px;top:340px;width:976px;height:1px;background:#3a3a3a}
  .footer .copyright{position:absolute;left:0;width:1200px;top:384px;text-align:center;font-size:14px}
</style>
</head>
<body>

<header>
  <div class="logo">Brammvok</div>
  <nav class="nav">
    <a class="active">Home</a><a>About Us</a><a>Category</a><a>Blog</a><a>Shop</a><a>Contact</a>
  </nav>
  <a class="btn login">LOGIN</a>
  <div class="cart">
    <span class="cart-dot">
      <svg width="18" height="18" viewBox="0 0 24 24" fill="none" stroke="#fff" stroke-width="2" stroke-linecap="round" stroke-linejoin="round"><path d="M3 4h2l2.4 11h10.2l2-8H6.3"/><circle cx="9" cy="19.5" r="1.3"/><circle cx="17" cy="19.5" r="1.3"/></svg>
    </span>
    CART
  </div>
</header>

<section class="hero" role="img" aria-label="Living room with a cream sofa, cushions and wooden furniture against a terracotta wall">
  <div class="hero-shade"></div>
  <div class="hero-text">
    <div class="eyebrow">Welcome To</div>
    <h1>Brammvok Hand<br>-Crafted Furniture</h1>
    <p>Lorem ipsum dolor sit amet, consectetur adipiscing.</p>
    <a class="btn">GET STARTED</a>
  </div>
</section>

<h2 class="section-title" style="top:722px">OUR CATEGORY</h2>
<div class="tabs">
  <div class="tab active">1 COLLECTIONS</div>
  <div class="tab">2 COLLECTIONS</div>
  <div class="tab">3 COLLECTIONS</div>
</div>

<article class="cat" style="left:128px">
  <h3>ROCKERS</h3>
  <div class="count">1 COLLECTIONS</div>
  <a class="btn">BUY NOW</a>
  <div class="photo" role="img" aria-label="Wooden rocking chair" style="background:linear-gradient(160deg,#efe6d8,#c59a6a 60%,#e9dfd0)"></div>
</article>
<article class="cat" style="left:455px">
  <h3>CHAIRS</h3>
  <div class="count">1 COLLECTIONS</div>
  <a class="btn">BUY NOW</a>
  <div class="photo" role="img" aria-label="Green upholstered chair on wooden legs" style="background:linear-gradient(160deg,#eee8dc,#7f8f3a 55%,#e9e0d2)"></div>
</article>
<article class="cat" style="left:782px">
  <h3>LOUNGE CHAIRS</h3>
  <div class="count">1 COLLECTIONS</div>
  <a class="btn">BUY NOW</a>
  <div class="photo" role="img" aria-label="Folding wooden lounge chair with cream fabric" style="background:linear-gradient(160deg,#efe7da,#c08a52 55%,#ebe2d4)"></div>
</article>

<div class="tile" style="left:128px;background:linear-gradient(135deg,#9a8a72,#c7b79b 50%,#6b5a44)" role="img" aria-label="Rattan sofa with cushions">
  <div class="dim"></div>
  <div class="label">SOFA</div>
  <a class="btn">SHOP NOW</a>
</div>
<div class="tile" style="left:632px;background:linear-gradient(135deg,#5e6b4a,#8f7a5c 50%,#3f3a2c)" role="img" aria-label="Wooden rocking chair on a porch">
  <div class="dim"></div>
  <div class="label">CHAIR</div>
  <a class="btn">SHOP NOW</a>
</div>

<section class="about">
  <div class="photo" role="img" aria-label="Craftsman working on wooden furniture in a workshop"></div>
  <h2>ABOUT BRAMMVOK HAND<br>-CRAFTED FURNITURE</h2>
  <div class="copy">
    <p>Lorem ipsum dolor sit amet, consectetur adipiscing elit, sed do eiusmod tempor incididunt ut labore et dolore magna aliqua. Quis ipsum suspendisse ultrices gravida. Risus commodo viverra maecenas accumsan lacus vel facilisis.</p>
    <p>Lorem ipsum dolor sit amet, consectetur adipiscing elit, sed do eiusmod tempor incididunt ut labore et dolore magna aliqua. Quis ipsum suspendisse ultrices gravida. Risus commodo viverra maecenas accumsan.</p>
  </div>
  <a class="btn">LEARN MORE</a>
</section>

<h2 class="section-title" style="top:2646px">OUR BLOG</h2>

<article class="post" style="left:112px">
  <div class="photo" role="img" aria-label="Rustic wooden kitchen interior" style="background:linear-gradient(135deg,#d9cbb6,#8a6a4c 55%,#c8b49a)"></div>
  <h4>LOREM IPSUM DOLOR SIT AMET,<br>CONSECTETUR ADIPISCING</h4>
  <div class="date">JAN 10, 2024</div>
  <div class="more">LEARN MORE</div>
</article>
<article class="post" style="left:444px">
  <div class="photo" role="img" aria-label="Hands carving a wooden panel" style="background:linear-gradient(135deg,#5a2e1e,#9a5a38 50%,#3a2016)"></div>
  <h4>LOREM IPSUM DOLOR SIT AMET,<br>CONSECTETUR ADIPISCING</h4>
  <div class="date">JAN 10, 2024</div>
  <div class="more">LEARN MORE</div>
</article>
<article class="post" style="left:776px">
  <div class="photo" role="img" aria-label="Wooden bench with colourful striped cushions" style="background:linear-gradient(135deg,#e7dccb,#d4653a 45%,#7a5a3e 80%)"></div>
  <h4>LOREM IPSUM DOLOR SIT AMET,<br>CONSECTETUR ADIPISCING</h4>
  <div class="date">JAN 10, 2024</div>
  <div class="more">LEARN MORE</div>
</article>

<footer class="footer">
  <div class="logo">Brammvok</div>
  <p class="about-text">Lorem ipsum dolor sit amet, consectetur adipiscing elit, sed do eiusmod tempor incididunt ut labore et dolore magna aliqua.</p>
  <div class="fcol" style="left:560px">
    <h4>QUICK LINKS</h4>
    <ul><li>Home</li><li>About Us</li><li>Category</li><li>Blog</li><li>Shop</li><li>Contact</li></ul>
  </div>
  <div class="fcol" style="left:760px">
    <h4>SUPPORT</h4>
    <ul><li>Delivery and Returns</li><li>Order Status</li><li>Warranty</li><li>Returns</li></ul>
  </div>
  <div class="fcol" style="left:962px">
    <h4>CONTACT US</h4>
    <ul><li>Pagefold</li><li>Chirpwell</li><li>Workthread</li></ul>
  </div>
  <div class="rule"></div>
  <div class="copyright">©Copyrights 2024 Brammvok &nbsp;|&nbsp; All Rights Reserved</div>
</footer>

</body>
</html>
```